Brennock Metal recycling, a business card/logo for our industrial family metal recycling company

A new business card design/logo for our long established family metal recycling company.
I have a logo for our property company which was designed a few months ago on pixel forum which I would like to be very close to this design but have a more industrial feel to it and in a darker blue colour, please see attachments.

Target Market(s)

industries that produce metal waste for recycling, construction sites, engineering companies, manufactures, builders, plumbers, electricians, general house holders.

Industry/Entity Type

Recycling

Contact Information for Business Card

owner/director...Gordon brennock
e-mail....info@brennockscrapworks.example.co.uk
web address.....brennockscrapworks.example.co.uk

Font styles to use
Serif
Sans Serif

Colors
0255a3
ffffff

Requirements
Must have
• -dark blue business card on front.
-white on the back, see contact details, e-mail address for metal company.
-to have an industrial feel to it.
-brennock logo as business card attached but (brennock metal recycling)
please remove the little roof/arrow above brennock as this was relevant to property company.
Nice to have
• please see our website brennockscrapworks.example.co.uk with all details
being correct however I would like to refresh the logo to more like the brennock property investment business card logo attached.
Should not have
• should not contain details from property investments card as this design is for the metal recycling company.

```html
<!DOCTYPE html>
<html lang="en">
<head>
<meta charset="utf-8">
<title>Brennock Metal Recycling – Business Card</title>
<link href="https://fonts.googleapis.com/css2?family=Lato:wght@300;400;700;900&display=swap" rel="stylesheet">
<style>
  :root {
    --backdrop: #2f2a27;
    --brand-blue: #233578;
    --ink: #1a1a1a;
    --muted: #6b6b6b;
    --paper: #ffffff;
  }
  * { box-sizing: border-box; margin: 0; padding: 0; }
  html, body { width: 1200px; height: 847px; overflow: hidden; }
  body {
    background: var(--backdrop);
    font-family: "Lato", sans-serif;
    position: relative;
  }
  .card {
    position: absolute;
    width: 530px;
    height: 303px;
    box-shadow: 0 10px 24px rgba(0,0,0,.45);
  }
  .card-front {
    left: 50px; top: 120px;
    background: var(--brand-blue);
    color: var(--paper);
  }
  .card-back {
    left: 620px; top: 420px;
    background: var(--paper);
    border-bottom: 4px solid var(--brand-blue);
  }
  .wordmark {
    position: absolute;
    font-weight: 300;
    font-size: 84px;
    line-height: 1;
    letter-spacing: 1px;
    text-transform: lowercase;
  }
  .tagline {
    position: absolute;
    font-weight: 400;
    font-size: 15px;
    letter-spacing: 9px;
    text-transform: uppercase;
  }
  .card-front .wordmark { left: 110px; top: 50px; color: var(--paper); }
  .card-front .tagline { left: 114px; top: 140px; color: var(--paper); }
  .payment-methods {
    position: absolute;
    left: 0; right: 0; bottom: 38px;
    text-align: center;
    font-size: 11.5px;
    letter-spacing: .4px;
    text-transform: uppercase;
  }
  .card-back .wordmark { left: 175px; top: 42px; color: var(--ink); }
  .card-back .tagline { left: 179px; top: 132px; color: var(--muted); }
  .holder {
    position: absolute;
    left: 26px; top: 190px;
    width: 180px;
    text-align: right;
  }
  .holder-name {
    font-weight: 900;
    font-size: 21px;
    letter-spacing: -.3px;
    color: var(--ink);
  }
  .holder-name .given { color: var(--brand-blue); }
  .holder-role {
    font-weight: 300;
    font-size: 14px;
    color: var(--muted);
    margin-top: 4px;
  }
  .divider {
    position: absolute;
    left: 218px; top: 190px;
    width: 1.5px; height: 62px;
    background: var(--brand-blue);
  }
  .contact-list {
    position: absolute;
    left: 234px; top: 188px;
    list-style: none;
  }
  .contact-list li {
    display: flex;
    align-items: center;
    gap: 8px;
    font-size: 13.5px;
    color: #444;
    height: 22px;
  }
  .contact-list svg { width: 14px; height: 14px; flex: none; }
</style>
</head>
<body>

<section class="card card-front" aria-label="Card front">
  <div class="wordmark">brennock</div>
  <div class="tagline">Metal Recycling</div>
  <p class="payment-methods">Instant cash • Fast bank transfer • Pre paid Payra card • Printed cheque</p>
</section>

<section class="card card-back" aria-label="Card back">
  <div class="wordmark">brennock</div>
  <div class="tagline">Metal Recycling</div>

  <div class="holder">
    <div class="holder-name"><span class="given">Gordon</span> Brennock</div>
    <div class="holder-role">Owner/Director</div>
  </div>

  <div class="divider"></div>

  <ul class="contact-list">
    <li>
      <svg viewBox="0 0 24 24" aria-hidden="true"><path fill="#233578" d="M6.6 10.8a15 15 0 0 0 6.6 6.6l2.2-2.2a1 1 0 0 1 1-.25 11.4 11.4 0 0 0 3.6.57 1 1 0 0 1 1 1V20a1 1 0 0 1-1 1A17 17 0 0 1 3 4a1 1 0 0 1 1-1h3.5a1 1 0 0 1 1 1c0 1.25.2 2.45.57 3.57a1 1 0 0 1-.25 1z"/></svg>
      020-8000-4417
    </li>
    <li>
      <svg viewBox="0 0 24 24" aria-hidden="true"><rect x="2" y="5" width="20" height="14" rx="1" fill="#233578"/><path d="M2 6l10 7 10-7" fill="none" stroke="#fff" stroke-width="1.6"/></svg>
      info@brennockscrapworks.example.co.uk
    </li>
    <li>
      <svg viewBox="0 0 24 24" aria-hidden="true"><g fill="none" stroke="#233578" stroke-width="1.8"><circle cx="12" cy="12" r="9"/><ellipse cx="12" cy="12" rx="4" ry="9"/><path d="M3 12h18M5 7.5h14M5 16.5h14"/></g></svg>
      www.brennockscrapworks.example.co.uk
    </li>
  </ul>
</section>

</body>
</html>
```